DISCUSSION TOPICS: Launching Miss Corinne’s New e-Commerce Business

A native PowerPoint presentation outlining topics to be considered by a young teenager in launching her new e-commerce shop, primarily selling clothes and dolls online. The project consists of a title slide and topics grouped into 10 sections plus a closing. (I have uploaded the native Word document for the ease of cutting & pasting.) The design and colors should appeal to a young, aspiring fashionista and entrepreneur. Corinne's overall message in her packages is motivational and very spiritual (religious). Please insert royalty free stock photos or graphics to break up the text, as you deem appropriate. For selection, please submit the cover slide and slides for the first two chapters, designated by number and color in the attached. (This will not be a lengthy presentation.) Each new chapter/number/color should begin on a new slide, and the pages should NOT be numbered, so the facilitator can select chapters at random and present them out of the sequence of the PowerPoint presentation. I also have uploaded my logo and tagline for Plume on Cedar. It need not be a central component of the design, but I would like it incorporated in some small way, perhaps on the title page or in the footer of each page, wherever you feel is most appropriate. I paid an expedite fee when I posted the project since, ideally, I would like to distribute the presentation on Friday, July 29. Many thanks for considering this project that is urgently anticipated by the young recipient.
Updates
Thank you for viewing my invitation to work on my DISCUSSION TOPICS project. Especially since the recipient will be a young girl, expediency is of a higher priority than corporate perfection. Of course, I am depending upon you for a lively, creative design so Corinne will enjoy looking at your slides while the facilitator walks her through the content. Ideally, I would like to send the presentation to the facilitator on Friday, July 29. (For time zone reference, I reside in Texas.) I do not require three separate designs as advertised on the ArtHarbor site. I would prefer to work with you on only one that you consider a very appropriate, good design rather than stretching your time too thin for the ideal delivery window by forcing alternate designs. Many thanks! Please feel very welcome to contact me with any questions or requests for clarification. -- Dolores

Target Market(s)
Teenagers for sales and the infirm for motivational and spiritual gifts
Industry/Entity Type
Seller on e-commerce sites like Threadly and Vendora
Colors
Designer to choose colors to be used in the design.
Requirements
Must have
- A bold, modern, creative yet simple design that will appeal to a young female recipient.

Nice to have
- Graphics and royalty-free photos to break up the monotony of the dense text

Should not have
- Do not number the pages so "chapters" can be pulled and presented out of sequence

```html
<!DOCTYPE html>
<html lang="en">
<head>
<meta charset="utf-8">
<title>Discussion Topics – Plume on Cedar</title>
<link href="https://fonts.googleapis.com/css2?family=Space+Grotesk:wght@500;700&family=Poppins:wght@400;500&display=swap" rel="stylesheet">
<style>
:root{
  --page:#e4e4e4;
  --slide:#ffffff;
  --ink:#111111;
  --body:#333333;
  --muted:#666666;
  --plum:#8e3a66;
  --plum-soft:#c9a3b8;
  --bar:#1f1f1f;
  --rule:#d8c3cf;
}
*{box-sizing:border-box;margin:0;padding:0}
html,body{width:1200px;height:4231px;overflow:hidden;background:var(--page)}
body{position:relative;font-family:"Poppins",sans-serif;color:var(--body)}
.slide{position:absolute;left:34px;width:1132px;height:637px;background:var(--slide);box-shadow:0 2px 6px rgba(0,0,0,.18);overflow:hidden}
.footer{position:absolute;left:0;right:0;bottom:0;height:39px;background:var(--bar);color:#fff;font-size:11px;display:flex;align-items:center;justify-content:center}
.title{position:absolute;left:0;right:0;text-align:center;font-family:"Space Grotesk",sans-serif;font-weight:700;color:var(--ink);letter-spacing:.5px}
.rule{position:absolute;height:4px;border-top:1px solid var(--rule);border-bottom:1px solid var(--rule)}
.rule::after{content:"";position:absolute;left:30%;right:30%;top:-1px;height:1px;background:var(--plum)}
.list{position:absolute;list-style:none;font-size:13px;line-height:34px;color:var(--body)}
.list>li{position:relative;padding-left:24px}
.list>li::before{content:"→";position:absolute;left:0;top:0;color:var(--plum);font-weight:500}
.sub{list-style:none;font-size:11px;line-height:23px;color:var(--muted);margin:2px 0 4px 4px}
.sub li{position:relative;padding-left:24px}
.sub li::before{content:"";position:absolute;left:0;top:7px;width:9px;height:9px;border-radius:50%;background:var(--ink)}
.photo{position:absolute}
.brand{position:absolute;display:flex;align-items:center;justify-content:center;gap:8px;font-family:"Poppins",sans-serif;font-weight:500;color:var(--plum);background:#fff}
.brand .dot{width:10px;height:10px;border-radius:50%;background:var(--plum)}
.note-box{position:absolute;border:1px solid #d9d9d9;padding:14px 10px;font-size:11.5px;line-height:24px;color:var(--ink);font-weight:500}
.note-box .tip{font-weight:400;color:var(--muted);font-size:10.5px;line-height:23px;margin-top:8px}
.thanks{position:absolute;left:0;right:0;top:270px;text-align:center;font-family:"Space Grotesk",sans-serif;font-weight:700;font-size:78px;color:#fff;letter-spacing:2px}
</style>
</head>
<body>

<!-- Slide: identity -->
<section class="slide" style="top:62px">
  <h1 class="title" style="top:28px;font-size:46px">WHO ARE YOU?</h1>
  <div class="rule" style="left:508px;top:93px;width:115px"></div>
  <ul class="list" style="left:31px;top:131px;width:560px">
    <li>What about you do you most want to project to your customers?</li>
    <li>What is your mission or top priorities for the business?</li>
    <li>Does the name of your business convey what you want to project about yourself or your mission?</li>
    <li>What color(s) come to mind when you think of what you want to project? Is your logo easily identifiable/recognizable and aligned with your business name or mission and your selected color(s)?
      <ul class="sub"><li>I’m sure your graphic design camp will be very helpful in this area. There also are many online tools to help kickstart the process or enhance an in-process logo.</li></ul>
    </li>
    <li>Is your tagline brief, memorable, and aligned with your business name or mission?</li>
    <li>How can you differentiate yourself from competitors? What makes shopping with you uniquely pleasant?</li>
  </ul>
  <div class="brand" style="left:600px;top:192px;width:474px;height:279px;font-size:26px" role="img" aria-label="Plume on Cedar logo"><span class="dot"></span>Plume on Cedar</div>
  <div class="footer">© 2020 All Rights Reserved</div>
</section>

<!-- Slide: customers -->
<section class="slide" style="top:758px">
  <h2 class="title" style="top:42px;font-size:28px">WHO ARE YOUR CUSTOMERS &amp; WHAT DO THEY MOST WANT?</h2>
  <div class="rule" style="left:525px;top:91px;width:108px"></div>
  <div class="photo" style="left:31px;top:107px;width:222px;height:362px;background:linear-gradient(160deg,#e9d3d1,#c79a9c 60%,#a8827c)" role="img" aria-label="Photo of a knitted doll in a pink dress"></div>
  <div class="photo" style="left:300px;top:128px;width:164px;height:100px;background:var(--plum)"></div>
  <div class="photo" style="left:247px;top:198px;width:266px;height:362px;background:linear-gradient(180deg,#8a8472,#d9d2c2 35%,#8f8f8f 70%,#6b4a2e)" role="img" aria-label="Photo of a stack of folded knit sweaters"></div>
  <div class="brand" style="left:44px;top:478px;width:151px;height:87px;font-size:12px" role="img" aria-label="Plume on Cedar logo"><span class="dot"></span>Plume on Cedar</div>
  <ul class="list" style="left:565px;top:214px;width:540px">
    <li>Is there a target demographic for your business?</li>
    <li>What is most important to that group of potential customers?</li>
    <li>Does your product meet the expectations of your target customers?
      <ul class="sub">
        <li>If you have significant doubts, what can you change about what you are offering?</li>
        <li>If your friends represent your target customer base, what do they think about your product?</li>
      </ul>
    </li>
    <li>How can you deliver what your target customers most want if it’s intangible?</li>
  </ul>
  <div class="footer">© 2020 All Rights Reserved</div>
</section>

<!-- Slide: profit -->
<section class="slide" style="top:1450px">
  <h2 class="title" style="top:36px;font-size:36px">WILL YOU PROFIT FINANCIALLY?</h2>
  <div class="rule" style="left:510px;top:88px;width:112px"></div>
  <div class="brand" style="left:953px;top:20px;width:135px;height:82px;font-size:11px" role="img" aria-label="Plume on Cedar logo"><span class="dot"></span>Plume on Cedar</div>
  <ul class="list" style="left:31px;top:120px;width:560px">
    <li>What is the expected price tolerance of your customers?</li>
    <li>Define the profit margin you want to achieve on every sale.
      <ul class="sub"><li>Threadly customers want to negotiate a lower price and discounted shipping. Take both into account when you list the price of an item. Don’t mark up your product(s) too much, be reasonable and competitive, but include a small cushion for negotiating, as needed.</li></ul>
    </li>
    <li>Can you realize a profit at your price less your costs (e.g., product acquisition or creation, packaging supplies, shipping costs)?
      <ul class="sub">
        <li>Calculate your per unit cost to include items like product acquisition or creation, custom branding pieces (if appropriate), start-up expenses (e.g., mannequin, clothing rack, light ring), packaging supplies, shipping costs, etc.</li>
        <li>Other than for tax purposes, when calculating the per unit cost during the launch phase do not include costs for your workspace or “warehouse”, your business-related transportation, your salary, office supplies (e.g., paper, stapler, scissors, pens, monthly phone and internet charges), depreciation of office equipment (e.g., printer, computer/laptop, smart phone with camera), etc.</li>
      </ul>
    </li>
  </ul>
  <ul class="sub" style="position:absolute;left:597px;top:150px;width:500px">
    <li>If you plan to file taxes, keep a spreadsheet from the very beginning with all the aforementioned costs, packaging supplies, shipping costs, and anything else that can be deducted. All those costs will be subtracted from your sales/profit to, hopefully, realize a loss on paper for up to three years. After three years of losses, the IRS no longer considers the business viable. (Please confirm with a CPA and discuss the path forward relative to income tax, sales tax, etc.)</li>
  </ul>
  <div class="photo" style="left:639px;top:342px;width:172px;height:206px;border-radius:40%;background:radial-gradient(circle at 50% 40%,#f0b35a,#e0762a 60%,#fff 61%)" role="img" aria-label="Photo of a rag doll with orange hair and green overalls"></div>
  <div class="photo" style="left:852px;top:399px;width:230px;height:131px;border-radius:45%;background:radial-gradient(ellipse at 50% 50%,#f3d4e4,#e7b9cf 60%,#fff 62%)" role="img" aria-label="Photo of a baby doll in a pink outfit"></div>
  <div class="footer">© 2020 All Rights Reserved</div>
</section>

<!-- Slide: marketing -->
<section class="slide" style="top:2142px">
  <div class="photo" style="left:0;top:0;width:527px;height:598px;background:linear-gradient(120deg,#5d6b45 0%,#d9c2b0 30%,#e6cfc6 60%,#cfa9a3 100%)" role="img" aria-label="Photo of a woman in a pink belted jumpsuit beside palm leaves"></div>
  <div class="brand" style="left:384px;top:30px;width:128px;height:77px;font-size:11px" role="img" aria-label="Plume on Cedar logo"><span class="dot"></span>Plume on Cedar</div>
  <h2 class="title" style="left:565px;right:auto;top:50px;font-size:22px;line-height:35px;text-align:left">GET THE WORD OUT IF AND WHEN YOU<br>PLAN TO EXPAND BEYOND THREADLY</h2>
  <div class="rule" style="left:565px;top:130px;width:134px"></div>
  <ul class="list" style="left:565px;top:148px;width:535px;font-size:12.5px;line-height:23px">
    <li>Send a sample of your product to influencers or popular bloggers who represent your target demographic and tell your unique story via a carefully crafted one-page, single-sided flyer. Include photos! It’s not marketing, per se, it’s your story, what led you (a young lady of 11 years of age) to launch a business, not just any business but the product(s) you selected, and anything else that sets you apart from your contemporaries.
      <ul class="sub">
        <li>If it isn’t feasible to send a sample of your product, send only the professional looking flyer.</li>
        <li>Use much of the flyer information in your Threadly profile. People read them and they like photos.</li>
      </ul>
    </li>
    <li style="line-height:29px">Send a sample of your product and/or the flyer to select local newspapers or community newsletters that are read by your target demographic or those who might gift your product to that customer. Ask for a feature interview.</li>
    <li style="line-height:29px">Create a concise, memorable, and attractive marketing piece and post it on Pictogram, Friendbook, and any other platform that your target customers frequent.</li>
  </ul>
  <div class="footer">© 2020 All Rights Reserved</div>
</section>

<!-- Slide: branding -->
<section class="slide" style="top:2835px">
  <h2 class="title" style="top:38px;font-size:36px">BRAND EVERYTHING!</h2>
  <div class="rule" style="left:510px;top:90px;width:112px"></div>
  <div class="brand" style="left:972px;top:25px;width:116px;height:70px;font-size:10px" role="img" aria-label="Plume on Cedar logo"><span class="dot"></span>Plume on Cedar</div>
  <div class="note-box" style="left:31px;top:122px;width:527px;height:80px">Typically, the launch phase cannot support the cost of custom boxes and tissue paper with your logo (and tagline), professionally printed cards and stickers, etc.</div>
  <div class="note-box" style="left:31px;top:210px;width:527px;height:181px">You can more economically brand everything by purchasing blank stickers, folded notecards, postcards and whatever else you need, and printing on them your selected border, logo, tagline, text, etc.
    <div class="tip">Tip: Labelcraft supplies many templates for their labels, or you can design your stickers and cards on several online services but be wary of those that do not allow download of your design and provide only professional printing of your design.</div>
  </div>
  <div class="note-box" style="left:570px;top:122px;width:527px;height:269px">To ensure your brand/logo is what customers first see upon receiving a package from you, I suggest not reusing boxes from online retailers. Those boxes have the retailer’s printed logo, tape, shipping labels, etc. Although it’s economical to repurpose those boxes, it does not provide a “clean” first impression to your customers.
    <div class="tip">Tip: I purchase appropriately sized, lightweight shipping boxes from Boxwell.com. (Most are brown but some are white, which is preferred to highlight your logo sticker.) Order quantities can be as low as 10 boxes that are shipped for next-day delivery. Shipping costs are relatively high, so ensure your box size fits your product and, in the beginning, purchase enough for only one month.</div>
  </div>
  <div class="photo" style="left:31px;top:425px;width:337px;height:143px;background:linear-gradient(90deg,#f3f1ee,#d8c6b2 40%,#c97a3a 70%,#f3f1ee)" role="img" aria-label="Photo of a flat-lay outfit with sweater, bag and shoes"></div>
  <div class="photo" style="left:395px;top:425px;width:337px;height:143px;background:linear-gradient(90deg,#f6f3ef,#b9825a 45%,#e9d8c6 65%,#f6f3ef)" role="img" aria-label="Photo of a stack of folded brown sweaters"></div>
  <div class="photo" style="left:759px;top:425px;width:337px;height:143px;background:linear-gradient(90deg,#b3121c,#d8303a 45%,#e8c08a 70%,#a9101a)" role="img" aria-label="Photo of a fashion doll among red roses"></div>
  <div class="footer">© 2020 All Rights Reserved</div>
</section>

<!-- Slide: closing -->
<section class="slide" style="top:3529px;background:linear-gradient(135deg,#2a2020,#1d1717 50%,#2d2222)" role="img" aria-label="Dark photo of a woman seated on a chair">
  <div class="thanks">THANK YOU</div>
  <div class="footer" style="background:var(--plum)">© 2020 All Rights Reserved</div>
</section>

</body>
</html>
```